Pomelo - Website for fruit & juice

- The location of the outlet is Fort Kochi in India.
- Fort Kochi is a tourist destination. And it attracts majorly French and Portuguese tourist due to the history of the place.
- The location had plenty of food joints & mostly provide local foods only without giving much options to tourist.
- Road side fruit shops don't look hygienic
- At Pomelo we are going to sell fresh fruits as well as fruit juices.
- Customers can pick their fruits and Pomelo staffs will squeeze/blend or slice it for them.
- There will be no e-commerce on the site (no buying of products through site)

Target Market(s)

Tourist & health conscious individuals who want to have fresh fruit or juice.

Coding

Coded - Design and coding required

Number of Pages Required

4 page

Font styles to use
Script

Colors

Designer to choose colors to be used in the design.

Requirements
Must have
• Back End. Editable website.
• Since it for fruits & juices, we will be selling fruits as per season or availability.
• Editable or back end will allow us to add or delete menus as per availability.
• The project much have 4 pages. Namely:
• - Home
• - Concept
• - Menu
• - Location & Contact
Nice to have
• Fresh feel of the website
Should not have
• E-commerce

```html
<!DOCTYPE html>
<html lang="en">
<head>
<meta charset="utf-8">
<title>Pomelo – Fresh Fruit &amp; Juice</title>
<link rel="stylesheet" href="https://fonts.googleapis.com/css2?family=Lato:wght@400;700;900&family=Open+Sans:wght@700;800&display=swap">
<style>
  :root {
    --orange: #f56b12;
    --orange-deep: #f25a0e;
    --green: #157a26;
    --ink: #1d1d1d;
    --white: #ffffff;
    --black: #000000;
  }
  * { box-sizing: border-box; margin: 0; padding: 0; }
  html, body { width: 1200px; height: 2585px; overflow: hidden; }
  body { position: relative; background: var(--white); font-family: "Lato", sans-serif; color: var(--ink); }

  .site-header { position: absolute; top: 0; left: 0; width: 1200px; height: 137px; }
  .brand { position: absolute; left: 76px; top: 44px; font-family: "Lato", sans-serif; font-weight: 700; font-size: 44px; line-height: 1; color: var(--green); }
  .main-nav { position: absolute; right: 73px; top: 62px; display: flex; gap: 43px; }
  .main-nav a { font-weight: 700; font-size: 15px; color: var(--ink); text-decoration: none; }
  .main-nav a.is-active { color: var(--orange); }

  .hero { position: absolute; top: 137px; left: 0; width: 1200px; height: 561px;
    background: linear-gradient(100deg, #6d6a68 0%, #8a7a6c 30%, #a0703e 55%, #b9a47e 75%, #8e4a2b 100%);
    text-align: center; color: var(--white); }
  .hero::after { content: ""; position: absolute; inset: 0; background: rgba(0,0,0,.18); }
  .hero-content { position: relative; z-index: 1; }
  .hero-title { font-family: "Open Sans", sans-serif; font-weight: 800; font-size: 76px; letter-spacing: 1px; margin-top: 152px; line-height: 1; }
  .hero-lead { font-family: "Open Sans", sans-serif; font-weight: 700; font-size: 24px; line-height: 32px; margin: 22px auto 0; width: 740px; }
  .btn { display: inline-block; width: 189px; height: 48px; line-height: 48px; background: var(--orange);
    color: var(--white); font-family: "Open Sans", sans-serif; font-weight: 700; font-size: 18px; text-align: center; }
  .hero .btn { margin-top: 30px; }
  .slider-dots { display: flex; justify-content: center; gap: 7px; margin-top: 121px; }
  .slider-dots span { width: 14px; height: 14px; border-radius: 50%; background: var(--white); }
  .slider-dots span.is-current { border: 3px solid var(--green); }

  .feature-photo { position: absolute; left: 75px; width: 1051px; height: 340px; }
  .feature-photo::after { content: ""; position: absolute; inset: 0; background: rgba(0,0,0,.28); }
  .feature-title { position: absolute; left: 0; width: 1200px; text-align: center; color: var(--white);
    font-weight: 900; font-size: 76px; line-height: 1; z-index: 2; }
  .info-card { position: absolute; left: 164px; width: 872px; height: 302px; background: var(--green);
    color: var(--white); text-align: center; z-index: 2; padding-top: 38px; }
  .info-card h3 { font-weight: 700; font-size: 27px; letter-spacing: .3px; }
  .info-card p { font-size: 16.5px; line-height: 28px; width: 745px; margin: 12px auto 0; }
  .info-card .btn { margin-top: 24px; }

  .about-photo { top: 763px; background: linear-gradient(90deg, #6c7a3a 0%, #8c2a2e 25%, #b0753a 50%, #7a2a2c 75%, #4c3a30 100%); }
  .about-title { top: 850px; }
  .about-card { top: 992px; }

  .menu-band { position: absolute; top: 1351px; left: 0; width: 1200px; height: 350px;
    background: linear-gradient(90deg, #b8902a 0%, #d8b040 30%, #c89a48 55%, #e0a030 80%, #c8802a 100%);
    color: var(--white); text-align: center; }
  .menu-band::after { content: ""; position: absolute; inset: 0; background: rgba(0,0,0,.32); }
  .menu-content { position: relative; z-index: 1; }
  .menu-title { font-weight: 900; font-size: 60px; line-height: 1; margin-top: 68px; }
  .menu-lead { font-size: 17.5px; line-height: 31px; width: 940px; margin: 18px auto 0; }
  .menu-band .btn { margin-top: 30px; }

  .concept-photo { top: 1749px; background: linear-gradient(90deg, #5a6a6a 0%, #c07a3a 30%, #7a2a2a 48%, #c89a40 65%, #8a8a40 80%, #5a6066 100%); }
  .concept-title { top: 1835px; }
  .concept-card { top: 1978px; }

  .signup { position: absolute; top: 2335px; left: 0; width: 1200px; height: 89px;
    background: linear-gradient(90deg, var(--orange), var(--orange-deep)); }
  .signup-label { position: absolute; left: 235px; top: 30px; color: var(--white); font-weight: 700; font-size: 26px; }
  .signup-input { position: absolute; left: 441px; top: 24px; width: 359px; height: 44px; background: var(--white);
    font-size: 13px; color: #444; padding-left: 16px; line-height: 44px; }
  .signup-submit { position: absolute; left: 809px; top: 24px; width: 155px; height: 44px; background: var(--green);
    color: var(--white); font-weight: 700; font-size: 16px; text-align: center; line-height: 44px; }

  .site-footer { position: absolute; top: 2424px; left: 0; width: 1200px; height: 161px; background: var(--black);
    color: var(--white); text-align: center; }
  .footer-nav { display: flex; justify-content: center; gap: 46px; margin-top: 35px; }
  .footer-nav a { color: var(--white); text-decoration: none; font-weight: 700; font-size: 15px; }
  .copyright { font-size: 12px; margin-top: 19px; color: #ddd; }
  .social { display: flex; justify-content: center; gap: 24px; margin-top: 17px; }
  .social span { width: 22px; height: 22px; border-radius: 50%; background: var(--white); }
</style>
</head>
<body>
  <header class="site-header">
    <div class="brand">Pomelo</div>
    <nav class="main-nav">
      <a class="is-active" href="#">HOME</a>
      <a href="#">CONCEPT</a>
      <a href="#">MENU</a>
      <a href="#">ABOUT US</a>
      <a href="#">LOCATION</a>
    </nav>
  </header>

  <section class="hero" role="img" aria-label="Woman choosing fresh apples at a market fruit stall">
    <div class="hero-content">
      <h1 class="hero-title">FEEL FRESH</h1>
      <p class="hero-lead">We make juice from the fresh fruits that you pick up yourself from the fruit basket.</p>
      <span class="btn">Read More</span>
      <div class="slider-dots"><span class="is-current"></span><span></span><span></span><span></span></div>
    </div>
  </section>

  <div class="feature-photo about-photo" role="img" aria-label="Market display of apples, pears, grapes and pomegranates"></div>
  <h2 class="feature-title about-title">ABOUT US</h2>
  <section class="info-card about-card">
    <h3>AND HENCE POMELO:</h3>
    <p>As a health conscious customer, one has every right to know the fruit before she/he sips the first sip of juice made out of it. We at Pomelo insist our clientele to pick the fresh fruits themselves from our fruit baskets so they know what they are consuming. And we can blend or squeezed those fruits for them as per their wish i.e only fruit or fruit with some add-ons.</p>
    <span class="btn">Read More</span>
  </section>

  <section class="menu-band" role="img" aria-label="Close-up of sliced lemon, orange, kiwi and strawberry">
    <div class="menu-content">
      <h2 class="menu-title">MENU</h2>
      <p class="menu-lead">Lorem ipsum dolor sit amet, consectetur adipiscing elit. Vestibulum gravida neque ultricies, vestibulum lectus id, consequat ex. Duis sit amet elit vitae felis mollis pulvinar ac nec nisi.</p>
      <span class="btn">View Menu</span>
    </div>
  </section>

  <div class="feature-photo concept-photo" role="img" aria-label="Glasses and bottles of fresh juice with pineapple, bananas and citrus"></div>
  <h2 class="feature-title concept-title">CONCEPT</h2>
  <section class="info-card concept-card">
    <h3>ORIGIN OF THE CONCEPT:</h3>
    <p>Visit any fruit vendor and ask them what they do with the left over and if you are lucky enough you may get the truth. “They sell their leftover to the juice bar”<br>When you order a glass of juice from any place you may not have any idea about the condition of the fruit before it was squeezed &amp; served to you.</p>
    <span class="btn">Read More</span>
  </section>

  <section class="signup">
    <span class="signup-label">EMAIL SIGN UP</span>
    <span class="signup-input">ENTER EMAIL ADDRESS</span>
    <span class="signup-submit">SUBSCRIBE</span>
  </section>

  <footer class="site-footer">
    <nav class="footer-nav">
      <a href="#">HOME</a><a href="#">CONCEPT</a><a href="#">MENU</a><a href="#">ABOUT US</a><a href="#">LOCATION</a>
    </nav>
    <p class="copyright">Copyright © 2019 Company Name All Right reserved</p>
    <div class="social" aria-label="Social links"><span></span><span></span><span></span><span></span><span></span></div>
  </footer>
</body>
</html>
```